The Open Willow Gate Book Cover

Cover for Multiauthor Ebook & Paper Print Book Cover

Book Title:
The Open Willow Gate : Notes From Calmer Shores

This collaborative multiauthor book is a collection of stories of recovery and rising from addiction for those looking for hope and the courage to take their own open willow gate. Whether contemplating making the first step or having completed all 12 of them, recovery from alcohol, drug, codependency, eating, sex, shame, gambling, busyness, etc is a path we will always walk.

Target Market(s)

Humans looking for guidance and words of wisdom healing from addiction of all kinds - to know they aren't alone, to provide guidance, and to give them hope. Ages 16 and up. Any Gender. International. Looking for The Open Willow Gate in their recovery process and life.

Industry/Entity Type

Recovery, Addiction, Wellness

Font styles to use
Serif
Script

Colors
0054AA
0677BA
7BADD7
CADEEF
E8F1F8
FFF300
FFF600
FEFA6F
FFFEC7
FFFEE8

Requirements
Must have
• masculine and feminine elements, mostly Black & White but with some soft sunrise elements of color
Nice to have
• steps or stairs
Should not have
• anything that feels depressing, we want honest but hopeful

```html
<!DOCTYPE html>
<html lang="en">
<head>
<meta charset="utf-8">
<title>The Open Willow Gate : Notes From Calmer Shores</title>
<link rel="stylesheet" href="https://fonts.googleapis.com/css2?family=Cormorant+Garamond:wght@500;600&display=swap">
<style>
  :root {
    --page-bg: #e7e7e7;
    --cover-dark: #2e2e2e;
    --cover-deep: #1f1f1f;
    --beam-light: #e4e4b4;
    --beam-mid: #b9bd7a;
    --title-yellow: #fff300;
    --subtitle-white: #f4f4f4;
    --rule-grey: #8a8a8a;
  }
  * { margin: 0; padding: 0; box-sizing: border-box; }
  html, body {
    width: 1000px;
    height: 1200px;
    overflow: hidden;
    background: var(--page-bg);
  }
  .book-cover {
    position: absolute;
    left: 70px;
    top: 0;
    width: 860px;
    height: 1200px;
    background: var(--cover-dark);
    overflow: hidden;
  }
  .cover-scene {
    position: absolute;
    inset: 0;
    width: 100%;
    height: 100%;
  }
  .title {
    position: absolute;
    left: 0;
    top: 760px;
    width: 100%;
    font-family: "Cormorant Garamond", Georgia, serif;
    font-weight: 600;
    font-size: 108px;
    line-height: 92px;
    color: var(--title-yellow);
    letter-spacing: 1px;
  }
  .title-line { display: block; white-space: nowrap; }
  .title-line--the { padding-left: 560px; }
  .title-line--open { padding-left: 460px; }
  .title-line--willow { padding-left: 330px; }
  .title-line--gate { padding-left: 240px; }
  .subtitle {
    position: absolute;
    left: 0;
    top: 1118px;
    width: 100%;
    display: flex;
    align-items: center;
    justify-content: center;
    gap: 28px;
    font-family: "Cormorant Garamond", Georgia, serif;
    font-weight: 500;
    font-size: 38px;
    color: var(--subtitle-white);
  }
  .subtitle-rule {
    width: 110px;
    height: 1px;
    background: var(--rule-grey);
  }
</style>
</head>
<body>
  <main class="book-cover">
    <svg class="cover-scene" viewBox="0 0 860 1200" role="img" aria-label="Photograph from above of a lone walker crossing a concrete floor through a diagonal beam of warm sunlight">
      <defs>
        <linearGradient id="beamGradient" x1="1" y1="0" x2="0" y2="1">
          <stop offset="0" stop-color="#d6d8a0"/>
          <stop offset="0.45" stop-color="#b4b77a"/>
          <stop offset="1" stop-color="#5d5e4a"/>
        </linearGradient>
        <linearGradient id="shadeGradient" x1="0" y1="0" x2="1" y2="1">
          <stop offset="0" stop-color="#3a3a3a"/>
          <stop offset="1" stop-color="#2a2a2a"/>
        </linearGradient>
      </defs>
      <rect width="860" height="1200" fill="url(#shadeGradient)"/>
      <polygon points="470,0 860,0 860,420 0,1170 0,900" fill="url(#beamGradient)"/>
      <polygon points="860,420 860,1200 0,1200 0,1170" fill="#2b2b2b"/>
    </svg>

    <h1 class="title">
      <span class="title-line title-line--the">THE</span>
      <span class="title-line title-line--open">OPEN</span>
      <span class="title-line title-line--willow">WILLOW</span>
      <span class="title-line title-line--gate">GATE</span>
    </h1>

    <p class="subtitle">
      <span class="subtitle-rule"></span>
      <span class="subtitle-text">Notes From Calmer Shores</span>
      <span class="subtitle-rule"></span>
    </p>
  </main>
</body>
</html>
```